UI design for kiosk touch screen

We need a UI design for a touch screen device to be used by costumers in a store and show information about specific products. We're looking for a general concept to serve as a starting point and we're not expecting a fully coded design.
We envision a UI where it first shows a range of products; once touched, it should show information about the product which includes text, touchable photos, videos and document files. We're interested in the starting page and the product details page.
We are the suppliers of the device and not the owners of stores that will use them. The purpose of this design is for in-person demonstrations to potential clients or in ads so the design should be agnostic about the end product(s). You may freely pick random placeholder or fictional products and assets to showcase the design concept as long as they can be changed without compromising the design. You can use our logo (annexed) in the design as a placeholder but it's not necessary.
We're using web technologies to develop the UI so the same principles should apply, except some exceptions below:
- There's no need for a responsive design since the resolution is set at 1920x1080 on a 22'' monitor in landscape orientation.
- All interactions will be done using the touchscreen, so any interactive component needs to be large enough for navigation to be comfortable.
- The design should be visually engaging and eye-catching, more so than a regular website.
Physical shop owners.
Store
2 page

```html
<!DOCTYPE html>
<html lang="en">
<head>
<meta charset="utf-8">
<title>Product Details</title>
<link rel="stylesheet" href="https://fonts.googleapis.com/css2?family=Roboto:wght@400;500;700;900&family=Quicksand:wght@500;600&family=Noto+Sans:wght@400;600&display=swap">
<style>
:root{
  --bg:#e4f0f7;
  --card:#ffffff;
  --ink:#111111;
  --ink-soft:#2b2b2b;
  --blue:#1a73d9;
  --orange:#f7931e;
  --brand-purple:#5b1f8a;
  --photo-a:#8a8a8a;
  --photo-b:#4f4f4f;
}
*{box-sizing:border-box;margin:0;padding:0}
html,body{width:1200px;height:675px;overflow:hidden;background:var(--bg)}
.screen{position:relative;width:1200px;height:675px;background:var(--bg);font-family:"Noto Sans",sans-serif;color:var(--ink)}
.brand{position:absolute;left:32px;top:24px;font-family:"Roboto",sans-serif;font-weight:900;font-size:30px;color:var(--brand-purple);letter-spacing:-0.5px}
.page-title{position:absolute;left:0;width:1170px;top:20px;text-align:center;font-family:"Roboto",sans-serif;font-weight:700;font-size:36px;letter-spacing:-0.5px}
.back-btn{position:absolute;left:31px;top:93px;width:114px;height:37px;border:1.5px solid var(--blue);border-radius:19px;display:flex;align-items:center;justify-content:center;gap:10px;color:var(--blue);font-family:"Quicksand",sans-serif;font-weight:500;font-size:16px;background:transparent}
.card{position:absolute;left:31px;top:152px;width:1138px;height:438px;background:var(--card);border-radius:16px}
.media{position:absolute;left:44px;top:165px;width:534px;height:412px;overflow:hidden}
.media-main{position:absolute;left:0;top:0;width:534px;height:300px;background:linear-gradient(160deg,var(--photo-a),var(--photo-b))}
.play{position:absolute;left:216px;top:101px}
.thumbs{position:absolute;left:0;top:300px;width:534px;height:112px;display:flex}
.thumb{height:100%}
.t-pink{width:50px;background:#b98d8f}
.t-red{width:62px;background:#8a3a38}
.t-green{width:112px;background:#3f8a3a}
.t-purple{width:112px;background:#6b3a78}
.t-blue{width:112px;background:#3d4f86}
.t-olive{width:86px;background:#8f8455}
.nav-arrow{position:absolute;top:338px}
.nav-prev{left:12px}
.nav-next{right:12px}
.product-name{position:absolute;left:594px;top:158px;font-family:"Roboto",sans-serif;font-weight:700;font-size:37px;letter-spacing:-1px;color:var(--ink-soft)}
.badge-new{position:absolute;left:804px;top:157px;width:44px;height:44px;border-radius:50%;background:var(--orange);color:#fff;font-family:"Quicksand",sans-serif;font-weight:600;font-size:15px;display:flex;align-items:center;justify-content:center}
.price{position:absolute;right:44px;top:158px;font-family:"Roboto",sans-serif;font-weight:700;font-size:37px;letter-spacing:-0.5px;color:var(--ink-soft)}
.features{position:absolute;left:595px;top:225px;display:grid;grid-template-columns:206px 220px;row-gap:12px;list-style:none}
.features li{display:flex;align-items:center;gap:8px;font-family:"Quicksand",sans-serif;font-weight:500;font-size:19.5px;color:#222;height:23px}
.description{position:absolute;left:595px;top:350px;width:560px;font-size:14.6px;line-height:22.4px;letter-spacing:0.6px;color:#333}
.description p+p{margin-top:22px}
.tech-title{position:absolute;left:595px;top:505px;font-family:"Roboto",sans-serif;font-weight:500;font-size:14.5px;color:#111}
.docs{position:absolute;left:595px;top:540px;display:flex;gap:13px}
.doc-btn{width:150px;height:37px;border:1.5px solid var(--blue);border-radius:19px;display:flex;align-items:center;justify-content:center;gap:12px;color:var(--blue);font-family:"Quicksand",sans-serif;font-weight:500;font-size:15px}
.maker{position:absolute;left:1068px;top:614px;display:flex;align-items:center;gap:6px;font-family:"Roboto",sans-serif;font-weight:700;font-size:18px;color:var(--blue)}
.maker-mark{width:14px;height:14px;background:var(--blue)}
</style>
</head>
<body>
<div class="screen">
  <div class="brand">StyleHub</div>
  <h1 class="page-title">Product Details</h1>
  <div class="back-btn">
    <svg width="9" height="14" viewBox="0 0 9 14"><path d="M7 1 1 7l6 6" fill="none" stroke="currentColor" stroke-width="1.5"/></svg>
    Go Back
  </div>

  <div class="card"></div>

  <div class="media">
    <div class="media-main" role="img" aria-label="Product video: pair of grey sneakers on a wooden floor"></div>
    <svg class="play" width="98" height="98" viewBox="0 0 98 98">
      <circle cx="49" cy="49" r="46" fill="none" stroke="var(--orange)" stroke-width="3"/>
      <path d="M38 31v36l28-18z" fill="none" stroke="var(--orange)" stroke-width="3" stroke-linejoin="round"/>
    </svg>
    <div class="thumbs">
      <div class="thumb t-pink" role="img" aria-label="Colour option: pink sneakers"></div>
      <div class="thumb t-red" role="img" aria-label="Colour option: red sneakers"></div>
      <div class="thumb t-green" role="img" aria-label="Colour option: green sneakers"></div>
      <div class="thumb t-purple" role="img" aria-label="Colour option: purple sneakers"></div>
      <div class="thumb t-blue" role="img" aria-label="Colour option: blue sneakers"></div>
      <div class="thumb t-olive" role="img" aria-label="Colour option: olive sneakers"></div>
    </div>
    <svg class="nav-arrow nav-prev" width="20" height="46" viewBox="0 0 20 46"><path d="M18 2 2 23l16 21" fill="none" stroke="#fff" stroke-width="2.5"/></svg>
    <svg class="nav-arrow nav-next" width="20" height="46" viewBox="0 0 20 46"><path d="M2 2l16 21L2 44" fill="none" stroke="#fff" stroke-width="2.5"/></svg>
  </div>

  <div class="product-name">Comfy Racer</div>
  <div class="badge-new">new</div>
  <div class="price">$ 655</div>

  <ul class="features">
    <li><svg width="18" height="18" viewBox="0 0 18 18"><rect x="1" y="2" width="14" height="14" rx="2" fill="none" stroke="var(--blue)" stroke-width="1.6"/><path d="M4.5 8.5 8 12l8-9" fill="none" stroke="var(--blue)" stroke-width="1.8"/></svg>Ultra durable</li>
    <li><svg width="18" height="18" viewBox="0 0 18 18"><rect x="1" y="2" width="14" height="14" rx="2" fill="none" stroke="var(--blue)" stroke-width="1.6"/><path d="M4.5 8.5 8 12l8-9" fill="none" stroke="var(--blue)" stroke-width="1.8"/></svg>Extended warrenty</li>
    <li><svg width="18" height="18" viewBox="0 0 18 18"><rect x="1" y="2" width="14" height="14" rx="2" fill="none" stroke="var(--blue)" stroke-width="1.6"/><path d="M4.5 8.5 8 12l8-9" fill="none" stroke="var(--blue)" stroke-width="1.8"/></svg>Comfortable</li>
    <li><svg width="18" height="18" viewBox="0 0 18 18"><rect x="1" y="2" width="14" height="14" rx="2" fill="none" stroke="var(--blue)" stroke-width="1.6"/><path d="M4.5 8.5 8 12l8-9" fill="none" stroke="var(--blue)" stroke-width="1.8"/></svg>8 colours</li>
    <li><svg width="18" height="18" viewBox="0 0 18 18"><rect x="1" y="2" width="14" height="14" rx="2" fill="none" stroke="var(--blue)" stroke-width="1.6"/><path d="M4.5 8.5 8 12l8-9" fill="none" stroke="var(--blue)" stroke-width="1.8"/></svg>New design</li>
    <li><svg width="18" height="18" viewBox="0 0 18 18"><rect x="1" y="2" width="14" height="14" rx="2" fill="none" stroke="var(--blue)" stroke-width="1.6"/><path d="M4.5 8.5 8 12l8-9" fill="none" stroke="var(--blue)" stroke-width="1.8"/></svg>Free 2 blades</li>
  </ul>

  <div class="description">
    <p>Lorem ipsum dolor sit amet, consectetur adipisicing elit, sed do eiusmod tempor incididunt ut labore et dolore magna aliqua.</p>
    <p>Ut enim ad minim veniam, quis nostrud exercitation ullamco laboris nisi ut aliquip ex ea commodo consequat. Duis aute irure dolor in reprehenderit in voluptate velit esse cillum dolore eu fugiat nulla</p>
  </div>

  <div class="tech-title">Technical information</div>
  <div class="docs">
    <div class="doc-btn">Specifications<svg width="20" height="24" viewBox="0 0 20 24"><path d="M2 1h11l5 5v17H2z" fill="none" stroke="var(--blue)" stroke-width="1.4"/><path d="M13 1v5h5" fill="none" stroke="var(--blue)" stroke-width="1.4"/><rect x="0.5" y="13" width="13" height="7" fill="var(--blue)"/><path d="M6 9h8M6 11h8" stroke="var(--blue)" stroke-width="1"/></svg></div>
    <div class="doc-btn">Specifications<svg width="20" height="24" viewBox="0 0 20 24"><path d="M2 1h11l5 5v17H2z" fill="none" stroke="var(--blue)" stroke-width="1.4"/><path d="M13 1v5h5" fill="none" stroke="var(--blue)" stroke-width="1.4"/><rect x="0.5" y="13" width="13" height="7" fill="var(--blue)"/><path d="M6 9h8M6 11h8" stroke="var(--blue)" stroke-width="1"/></svg></div>
    <div class="doc-btn">Specifications<svg width="20" height="24" viewBox="0 0 20 24"><path d="M2 1h11l5 5v17H2z" fill="none" stroke="var(--blue)" stroke-width="1.4"/><path d="M13 1v5h5" fill="none" stroke="var(--blue)" stroke-width="1.4"/><rect x="0.5" y="13" width="13" height="7" fill="var(--blue)"/><path d="M6 9h8M6 11h8" stroke="var(--blue)" stroke-width="1"/></svg></div>
  </div>

  <div class="maker"><span class="maker-mark"></span>KIOVA</div>
</div>
</body>
</html>
```